Lumora Pathway Advisory - Business card design needed

I wish to get business cards designed so that it follows my website design ... http://www.lumora-pathway.org
I need logos for QUVEX 7 and KT Summit Associate for myself which I have uploaded the files.
I wish my qualifications PhD PMP FAICD to be smaller print than my name.
Regards
Leopold
Industry/Entity Type
Business
Contact Information for Business Card
Lumora Pathway Advisory
Dr Leopold Marsh PhD PMP FAICD
Director
PO Box 418 Kelvendale NSW 2093 AUSTRALIA
T:+61 2 9352 6710 M:+61 437 918000 F: +61 2 9368 2000
Email: leopold.marsh@lumora-pathway.org
Website: http://www.lumora-pathway.org

```html
<!DOCTYPE html>
<html lang="en">
<head>
<meta charset="utf-8">
<title>Lumora Pathway Advisory – Business Cards</title>
<link rel="stylesheet" href="https://fonts.googleapis.com/css2?family=Roboto+Condensed:wght@400;700&family=Roboto:wght@400;700&display=swap">
<style>
  :root {
    --stage-dark: #05070d;
    --stage-blue: #14233f;
    --navy-text: #2d3a6b;
    --panel-teal: #15303f;
    --label-blue: #8ea9d8;
    --url-blue: #6f87b8;
    --white: #ffffff;
    --band-deep: #1b2d5e;
    --band-mid: #4565ad;
    --band-light: #8ea6dc;
    --band-grey: #c9ced8;
    --badge-blue: #1a9ad6;
  }
  * { margin: 0; padding: 0; box-sizing: border-box; }
  html, body { width: 1029px; height: 1200px; overflow: hidden; }
  body {
    position: relative;
    background: var(--stage-dark);
    font-family: "Roboto", Arial, sans-serif;
  }
  .stage-backdrop {
    position: absolute; inset: 0;
    background: radial-gradient(ellipse at 85% 45%, var(--stage-blue) 0%, var(--stage-dark) 65%);
  }
  .card {
    position: absolute;
    left: 100px;
    width: 858px;
    height: 532px;
    background: var(--white);
    box-shadow: 0 6px 18px rgba(0,0,0,.6);
    overflow: hidden;
  }
  .card--front { top: 51px; }
  .card--back { top: 609px; }

  .tech-band {
    position: absolute; left: 0; width: 100%;
    background:
      linear-gradient(90deg, rgba(27,45,94,.0) 55%, rgba(201,206,216,.85) 88%, rgba(201,206,216,.5) 100%),
      linear-gradient(180deg, var(--band-light) 0%, var(--band-mid) 45%, var(--band-deep) 100%);
  }
  .card--front .tech-band--top { top: 0; height: 125px; }
  .card--front .tech-band--bottom { top: 458px; height: 74px; }
  .card--back .tech-band--top { top: 0; height: 129px; }
  .card--back .tech-band--bottom { top: 420px; height: 112px; }

  .title-bar {
    position: absolute; left: 0; top: 125px; width: 100%; height: 59px;
    background: var(--white);
  }
  .company-name {
    font-family: "Roboto Condensed", "Arial Narrow", sans-serif;
    font-weight: 700;
    color: var(--navy-text);
    font-size: 34px;
    text-transform: uppercase;
    letter-spacing: .3px;
    line-height: 1;
  }
  .title-bar .company-name { position: absolute; left: 17px; top: 12px; }

  .contact-panel {
    position: absolute; left: 0; top: 184px; width: 100%; height: 227px;
    background: var(--panel-teal);
  }
  .person-name {
    position: absolute; left: 48px; top: 26px;
    font-family: "Roboto Condensed", "Arial Narrow", sans-serif;
    font-weight: 700; font-size: 35px; color: var(--white); line-height: 1;
  }
  .person-name .credentials {
    font-size: 24px; color: var(--label-blue); margin-left: 6px;
  }
  .person-role {
    position: absolute; left: 48px; top: 70px;
    font-family: "Roboto Condensed", "Arial Narrow", sans-serif;
    font-weight: 700; font-size: 19px; color: var(--label-blue); line-height: 1;
  }
  .contact-list {
    position: absolute; top: 131px;
    list-style: none;
    font-size: 20px; font-weight: 700; color: var(--label-blue);
  }
  .contact-list li { height: 30px; line-height: 22px; display: flex; }
  .contact-list--phones { left: 63px; }
  .contact-list--online { left: 363px; }
  .contact-list .key { width: 60px; }
  .contact-list .sep { width: 26px; }
  .contact-list--online .key { width: 62px; }

  .address-bar {
    position: absolute; left: 0; top: 411px; width: 100%; height: 47px;
    background: var(--white);
    text-align: center; line-height: 47px;
    font-weight: 700; font-size: 20px; letter-spacing: 1.2px;
    color: var(--navy-text);
  }

  .badge { position: absolute; top: 466px; height: 54px; border-radius: 4px; }
  .badge--certification { left: 535px; width: 154px; background: var(--white); }
  .badge--partner { left: 700px; width: 140px; background: var(--badge-blue); border-radius: 2px; }

  .back-message {
    position: absolute; left: 0; top: 129px; width: 100%; height: 291px;
    background: var(--white);
    text-align: center;
  }
  .back-message .company-name { position: absolute; left: 0; right: 0; top: 106px; }
  .back-url {
    position: absolute; left: 0; right: 0; top: 148px;
    font-family: "Roboto Condensed", "Arial Narrow", sans-serif;
    font-weight: 700; font-size: 19px; color: var(--url-blue);
  }
  .tagline {
    position: absolute; left: 0; right: 0; top: 186px;
    font-weight: 700; font-size: 20px; letter-spacing: .8px; color: var(--navy-text);
  }
</style>
</head>
<body>
  <div class="stage-backdrop" role="img" aria-label="Dark blue backdrop with faint glowing digital squares"></div>

  <section class="card card--front">
    <div class="tech-band tech-band--top" role="img" aria-label="Blue digital block pattern with a pale human profile at the right"></div>
    <div class="title-bar"><h1 class="company-name">Lumora Pathway Advisory</h1></div>
    <div class="contact-panel">
      <p class="person-name">Dr. Leopold Marsh<span class="credentials">PhD, PMP, FAICD</span></p>
      <p class="person-role">DIRECTOR</p>
      <ul class="contact-list contact-list--phones">
        <li><span class="key">T</span><span class="sep">:</span><span>+61 2 9352 6710</span></li>
        <li><span class="key">M</span><span class="sep">:</span><span>+61 437 918000</span></li>
        <li><span class="key">F</span><span class="sep">:</span><span>+61 2 9368 2000</span></li>
      </ul>
      <ul class="contact-list contact-list--online">
        <li><span class="key">E</span><span class="sep">:</span><span>leopold.marsh@lumora-pathway.org</span></li>
        <li><span class="key">W</span><span class="sep">:</span><span>http://www.lumora-pathway.org</span></li>
      </ul>
    </div>
    <p class="address-bar">PO Box 418 Kelvendale NSW 2093 AUSTRALIA</p>
    <div class="tech-band tech-band--bottom" role="img" aria-label="Blue digital block pattern"></div>
    <div class="badge badge--certification" role="img" aria-label="QUVEX 7 certification badge"></div>
    <div class="badge badge--partner" role="img" aria-label="KT Summit Associate partner badge"></div>
  </section>

  <section class="card card--back">
    <div class="tech-band tech-band--top" role="img" aria-label="Blue digital block pattern with a pale human profile at the right"></div>
    <div class="back-message">
      <h2 class="company-name">Lumora Pathway Advisory</h2>
      <p class="back-url">http://www.lumora-pathway.org</p>
      <p class="tagline">We help you transform your business by transforming your IT.</p>
    </div>
    <div class="tech-band tech-band--bottom" role="img" aria-label="Blue digital block pattern"></div>
  </section>
</body>
</html>
```